Redesign for luxury lifestyle PR agency

Ginger Kite Otter is a luxury lifestyle public relations agency specialising in indigenous and regenerative travel. We are the elephant you want in the room. We represent interesting brands and people who would be described as changemakers in their respective fields. The winning design should be stylish, clean cut and earthy. It should communicate that Ginger Kite Otter is professional and representative of the industries that it serves. The purpose of the website is to provide clear information to potential customers and media, improve the image and brand of the company, position the company as one of scale and increase sales conversions. Its aesthetic will be aspirational and image led in an editorial style. I would like to be able to easily edit the website once finished and be able to work with the designer on an ad hoc basis once the project is completed.

Please see below for some website I like the style of:

https://www.velmora-ensemble.com/

https://www.tasbergglobal.com/

https://www.brindlequarterly.co.uk/

Pages I would like to include are:

Home
Services
Clients
Testimonials
About Us
News

I'm also attaching a proposal that I really liked the style of and I would like this sort of aesthetic on the website too. My logo is also attached (it is likely that the colour palette might change with the website).

I'm open to inspiration on the colours - my immediate preference is greens and/or blues.

Here is the existing website that I built myself on Wix - https://www.gingerkiteotter.com/ (it looks so outdated and amateur now hence the need of a serious rebrand)

Target Market(s)

Luxury travel and lifestyle brands

Industry/Entity Type

Luxury travel and lifestyle

Number of Pages Required

1 page

Font styles to use
Serif
Other font styles liked:
• Open to suggestions

Requirements
Must have
• Beautiful imagery

```html
<!DOCTYPE html>
<html lang="en">
<head>
<meta charset="utf-8">
<title>Ginger Kite Otter — Lifestyle PR</title>
<link href="https://fonts.googleapis.com/css2?family=Playfair+Display:wght@400;500;600&family=Montserrat:wght@400;500;600;700&display=swap" rel="stylesheet">
<style>
:root{
  --brand-blue:#0a9fd8;
  --wash:#dff2fa;
  --wash-deep:#cbe9f6;
  --navy:#1f2b6f;
  --ink:#1a1a1a;
  --body:#444;
  --muted:#8a8a8a;
  --white:#fff;
  --gold:#f2b01e;
  --serif:'Playfair Display', Georgia, serif;
  --sans:'Montserrat', Arial, sans-serif;
}
*{box-sizing:border-box;margin:0;padding:0}
html,body{width:1200px;height:4561px;overflow:hidden}
body{position:relative;background:var(--white);font-family:var(--sans);color:var(--ink)}
.abs{position:absolute}
a{color:inherit;text-decoration:none}

/* header */
.site-header{position:absolute;top:0;left:0;width:1200px;height:101px;background:var(--brand-blue)}
.brand{position:absolute;left:85px;top:25px;width:200px;height:152px;background:var(--white);box-shadow:0 4px 14px rgba(0,0,0,.12);display:flex;align-items:center;justify-content:center;text-align:center;font-family:var(--sans);font-weight:500;color:var(--brand-blue);font-size:22px;line-height:1.15;letter-spacing:.5px}
.main-nav{position:absolute;top:41px;left:580px;display:flex;gap:26px;font-size:13px;color:var(--white);font-weight:500}
.burger{position:absolute;left:1080px;top:44px;width:34px}
.burger span{display:block;height:2px;background:rgba(255,255,255,.8);margin-bottom:6px}
.burger span:last-child{width:22px;margin-left:12px}

/* shared */
.h-display{font-family:var(--serif);font-weight:400;color:var(--ink)}
.more{position:absolute;font-family:var(--serif);font-size:17px;color:var(--ink)}
.more svg{position:absolute;left:68px;top:20px}
.photo{position:absolute}

/* hero */
.hero-title{position:absolute;left:85px;top:228px;font-family:var(--serif);font-weight:600;font-size:53px;line-height:63px;width:440px}
.hero-rule{position:absolute;left:85px;top:447px;width:62px;height:6px;border-radius:3px;background:var(--navy)}
.hero-copy{position:absolute;left:85px;top:482px;width:400px;font-size:17.5px;line-height:25px;color:var(--body)}
.hero-card{position:absolute;top:209px;width:277px;height:434px;background:var(--white);box-shadow:0 6px 20px rgba(0,0,0,.08)}
.hero-card .photo{left:0;top:0;width:277px;height:354px}
.hero-card .label{position:absolute;left:24px;top:380px;font-family:var(--serif);font-weight:600;font-size:19px}
.hero-card svg{position:absolute;right:28px;top:386px}

/* services */
.services{position:absolute;top:749px;left:0;width:1200px;height:797px;background:linear-gradient(135deg,#e6f5fb 0%,#d6eef8 55%,#e4f4fb 100%)}
.services h2{position:absolute;left:85px;top:95px;font-size:50px}
.services .kicker{position:absolute;left:85px;top:165px;font-size:13px;font-weight:700}
.services .intro{position:absolute;left:85px;top:184px;width:560px;font-size:13px;line-height:21px;color:var(--body)}
.service{position:absolute;top:253px;width:238px}
.service .photo{position:relative;width:238px;height:269px}
.service h3{font-family:var(--serif);font-weight:500;font-size:18px;line-height:26px;margin-top:24px}
.service p{font-size:13px;line-height:21px;color:var(--body);margin-top:8px;width:230px}

/* about */
.about-title{position:absolute;left:673px;top:1678px;font-size:50px}
.about-copy{position:absolute;left:673px;top:1754px;width:412px;font-size:13px;line-height:21px;color:var(--body)}
.about-copy p+p{margin-top:13px}

/* clients */
.clients{position:absolute;top:2254px;left:0;width:1200px;height:462px;background:var(--wash)}
.clients h2{position:absolute;left:85px;top:96px;font-size:50px}
.clients .intro{position:absolute;left:85px;top:170px;width:250px;font-size:13px;line-height:21px;color:var(--body)}
.clients .photo{top:107px;height:247px}

/* news */
.news-title{position:absolute;left:85px;top:2806px;font-size:50px}
.news-card{position:absolute;top:2899px;width:326px;height:556px;background:var(--white);box-shadow:0 6px 20px rgba(0,0,0,.07)}
.news-card .photo{left:0;top:0;width:326px;height:333px}
.news-card .meta{position:absolute;left:34px;top:366px;font-size:12px;font-weight:600;color:var(--navy)}
.news-card h3{position:absolute;left:34px;top:394px;width:250px;font-family:var(--serif);font-weight:500;font-size:17px;line-height:25px}
.news-card .more{left:34px;top:493px}

/* testimonials */
.testimonials{position:absolute;top:3561px;left:0;width:1200px;height:657px;background:var(--wash)}
.testimonials .map{position:absolute;left:70px;top:50px;width:1060px;height:560px;background:radial-gradient(ellipse at center,rgba(140,190,215,.28) 0%,rgba(223,242,250,0) 70%)}
.testimonials h2{position:absolute;left:0;width:1200px;text-align:center;top:98px;font-size:50px}
.testimonials .sub{position:absolute;left:330px;width:540px;top:176px;text-align:center;font-size:13px;line-height:21px;color:var(--body)}
.avatar{position:absolute;left:552px;top:234px;width:96px;height:96px;border-radius:50%;background:linear-gradient(160deg,#e89a2c,#5a3a22)}
.quote{position:absolute;left:190px;width:820px;top:360px;text-align:center;font-size:14px;line-height:21px;color:#222}
.stars{position:absolute;left:544px;top:456px;display:flex;gap:2px}
.person{position:absolute;left:0;width:1200px;text-align:center;top:505px;font-family:var(--serif);font-size:20px;color:var(--navy)}
.role{position:absolute;left:0;width:1200px;text-align:center;top:538px;font-size:13px;color:var(--muted)}

/* footer */
.footer-title{position:absolute;left:85px;top:4320px;font-family:var(--serif);font-size:27px}
.signup{position:absolute;left:790px;top:4318px;width:324px;height:32px;border-bottom:1px solid #cfcfcf;font-size:12px;color:var(--muted)}
.signup svg{position:absolute;right:0;top:2px}
.footer-nav{position:absolute;left:87px;top:4378px;display:flex;gap:28px;font-size:12px;font-weight:600}
.footer-call{position:absolute;left:85px;top:4408px;font-size:12px;color:var(--muted)}
.social{position:absolute;left:985px;top:4373px;display:flex;gap:24px}
.social span{width:14px;height:14px;border-radius:50%;background:var(--ink)}
.footer-mail{position:absolute;right:86px;top:4408px;font-size:12px;color:var(--muted)}
.copyright{position:absolute;left:85px;top:4486px;font-size:12px;color:var(--muted)}
</style>
</head>
<body>

<header class="site-header">
  <div class="brand">Ginger Kite<br>Otter</div>
  <nav class="main-nav"><a>Home</a><a>Services</a><a>Clients</a><a>Testimonials</a><a>About Us</a><a>News</a></nav>
  <div class="burger"><span></span><span></span></div>
</header>

<!-- hero -->
<h1 class="hero-title">The Elephant You Want In The Room</h1>
<div class="hero-rule"></div>
<p class="hero-copy">Ginger Kite Otter is a boutique lifestyle PR and communications agency helping brands get their voices heard in the UK.</p>
<a class="more" style="left:85px;top:578px">Read More<svg width="44" height="12" viewBox="0 0 44 12"><path d="M2 8 Q20 0 38 7" fill="none" stroke="#222" stroke-width="2" stroke-dasharray="3 3"/><path d="M34 3 L40 8 L33 10" fill="#222"/></svg></a>

<article class="hero-card" style="left:536px">
  <div class="photo" role="img" aria-label="Aerial view of an island town by deep blue sea" style="background:linear-gradient(180deg,#5fa8d8 0%,#b7c2c4 30%,#7a9fb3 55%,#1d5a8e 80%,#0f3f73 100%)"></div>
  <span class="label">Marlow PR</span>
  <svg width="10" height="16" viewBox="0 0 10 16"><path d="M2 2 L8 8 L2 14" fill="none" stroke="#111" stroke-width="2"/></svg>
</article>
<article class="hero-card" style="left:837px">
  <div class="photo" role="img" aria-label="White SUV parked on a sandy beach under blue sky" style="background:linear-gradient(180deg,#3f7fc6 0%,#8fb6df 50%,#d9c497 62%,#cfb27c 100%)"></div>
  <span class="label">The Drift</span>
  <svg width="10" height="16" viewBox="0 0 10 16"><path d="M2 2 L8 8 L2 14" fill="none" stroke="#111" stroke-width="2"/></svg>
</article>

<!-- services -->
<section class="services">
  <h2 class="h-display">Services We Offer</h2>
  <a class="more" style="left:950px;top:104px;font-size:16px">View All Services<svg width="44" height="12" viewBox="0 0 44 12" style="left:120px"><path d="M2 8 Q20 0 38 7" fill="none" stroke="#222" stroke-width="2" stroke-dasharray="3 3"/><path d="M34 3 L40 8 L33 10" fill="#222"/></svg></a>
  <p class="kicker">Pure and simple</p>
  <p class="intro">No-nonsense approach to launching new brands to the uk market, offering a completely bespoke service to include:</p>

  <div class="service" style="left:85px">
    <div class="photo" role="img" aria-label="Hand-drawn strategic planning sketch on paper" style="background:linear-gradient(160deg,#f4eccf,#e9e0c2 50%,#d8cfa8)"></div>
    <h3>Strategic Planning</h3>
    <p>Ginger Kite Otter is a boutique lifestyle PR and communications agency helping brands get their voices heard in the UK.</p>
  </div>
  <div class="service" style="left:349px">
    <div class="photo" role="img" aria-label="Jigsaw puzzle with a blue news piece" style="background:linear-gradient(160deg,#f1f1f1,#d9d9d9 45%,#2a5fb0 60%,#e4e4e4)"></div>
    <h3>Consumer Media Relations</h3>
    <p>Ginger Kite Otter is a boutique lifestyle PR and communications agency helping brands get their voices heard in the UK.</p>
  </div>
  <div class="service" style="left:612px">
    <div class="photo" role="img" aria-label="Blue word cloud about reputation management" style="background:linear-gradient(160deg,#0b2f66,#0f4a8f 50%,#0a2956)"></div>
    <h3>Reputation Management</h3>
    <p>Ginger Kite Otter is a boutique lifestyle PR and communications agency helping brands get their voices heard in the UK.</p>
  </div>
  <div class="service" style="left:876px">
    <div class="photo" role="img" aria-label="Hands holding a phone with social engagement icons" style="background:linear-gradient(160deg,#8ec6e4,#d7b89a 55%,#c79a78)"></div>
    <h3>Influencer Engagement</h3>
    <p>Ginger Kite Otter is a boutique lifestyle PR and communications agency helping brands get their voices heard in the UK.</p>
  </div>
</section>

<!-- about -->
<div class="photo" role="img" aria-label="Parisian building facade under a pink sunset sky" style="left:85px;top:1696px;width:209px;height:407px;background:linear-gradient(180deg,#c98ac9 0%,#a86aa6 35%,#4a3a44 70%,#2e2830 100%)"></div>
<div class="photo" role="img" aria-label="Portrait of the agency founder in a white jumper" style="left:296px;top:1654px;width:331px;height:492px;background:linear-gradient(180deg,#f2f2f2 0%,#e6e3df 50%,#f0efed 100%)"></div>
<h2 class="h-display about-title">About Us</h2>
<div class="about-copy">
  <p>Maren Holt founded Ginger Kite Otter in 2016 after working for one of the most reputable luxury travel PR agencies in London, leading a team that launched some of the world's most iconic hotels, as well as spending time at a national newspaper. She understands what it is like to be on either side of the PR coin and what it takes to create a juicy story.</p>
  <p>Ginger Kite Otter works as an extension to your team providing a service that feels in-house. Maren prefers a direct approach and will always pick up the phone to sound out an idea and probably ask what you're planning for dinner too. The Ginger Kite Otter clients are a carefully curated list and they feel like family.</p>
</div>
<a class="more" style="left:674px;top:2068px">Read More<svg width="44" height="12" viewBox="0 0 44 12"><path d="M2 8 Q20 0 38 7" fill="none" stroke="#222" stroke-width="2" stroke-dasharray="3 3"/><path d="M34 3 L40 8 L33 10" fill="#222"/></svg></a>

<!-- clients -->
<section class="clients">
  <h2 class="h-display">Clients</h2>
  <p class="intro">A dynamic collection of innovative lifestyle clients that we are wholly passionate about</p>
  <a class="more" style="left:86px;top:255px">View All Clients<svg width="44" height="12" viewBox="0 0 44 12" style="left:104px"><path d="M2 8 Q20 0 38 7" fill="none" stroke="#222" stroke-width="2" stroke-dasharray="3 3"/><path d="M34 3 L40 8 L33 10" fill="#222"/></svg></a>
  <div class="photo" role="img" aria-label="Crossed arms raised against a blue sky" style="left:388px;width:230px;background:linear-gradient(180deg,#7fb2dc,#9cc3e2 50%,#6b4a35)"></div>
  <div class="photo" role="img" aria-label="Restaurant storefront with a teal awning" style="left:643px;width:228px;background:linear-gradient(180deg,#c45a34 0%,#2bb3a8 18%,#1f1f22 45%,#2a2a2e 100%)"></div>
  <div class="photo" role="img" aria-label="Framed portrait painting on a white wall" style="left:898px;width:228px;background:radial-gradient(ellipse at center,#6d5a35 0%,#a08449 30%,#f0f0ee 55%)"></div>
  <div class="photo" role="img" aria-label="Table setting with cutlery" style="left:1153px;width:47px;background:linear-gradient(180deg,#6b6a55,#3a3a30)"></div>
</section>

<!-- news -->
<h2 class="h-display news-title">Latest News</h2>
<a class="more" style="left:1016px;top:2820px;font-size:16px">View All<svg width="44" height="12" viewBox="0 0 44 12" style="left:56px"><path d="M2 8 Q20 0 38 7" fill="none" stroke="#222" stroke-width="2" stroke-dasharray="3 3"/><path d="M34 3 L40 8 L33 10" fill="#222"/></svg></a>

<article class="news-card" style="left:85px">
  <div class="photo" role="img" aria-label="Cosy wooden cabin interior with blue sofa" style="background:linear-gradient(160deg,#e8e6e0,#b9864f 45%,#6b4a2c 70%,#1f3350)"></div>
  <p class="meta">22 July 2022 . By Admin</p>
  <h3>Ginger Kite Otter is a luxury lifestyle public relations agency</h3>
  <a class="more">Read More<svg width="44" height="12" viewBox="0 0 44 12"><path d="M2 8 Q20 0 38 7" fill="none" stroke="#222" stroke-width="2" stroke-dasharray="3 3"/><path d="M34 3 L40 8 L33 10" fill="#222"/></svg></a>
</article>
<article class="news-card" style="left:437px">
  <div class="photo" role="img" aria-label="Garden sculpture among tropical palms" style="background:linear-gradient(180deg,#4b6a3a,#6f8a55 45%,#9aa38c 65%,#e8e2d8)"></div>
  <p class="meta">22 July 2022 . By Admin</p>
  <h3>Ginger Kite Otter is a luxury lifestyle public relations agency</h3>
  <a class="more">Read More<svg width="44" height="12" viewBox="0 0 44 12"><path d="M2 8 Q20 0 38 7" fill="none" stroke="#222" stroke-width="2" stroke-dasharray="3 3"/><path d="M34 3 L40 8 L33 10" fill="#222"/></svg></a>
</article>
<article class="news-card" style="left:788px">
  <div class="photo" role="img" aria-label="Hammock strung over turquoise lagoon water" style="background:linear-gradient(180deg,#9ad0d2,#5fbcbc 50%,#3fa7a8)"></div>
  <p class="meta">22 July 2022 . By Admin</p>
  <h3>Ginger Kite Otter is a luxury lifestyle public relations agency</h3>
  <a class="more">Read More<svg width="44" height="12" viewBox="0 0 44 12"><path d="M2 8 Q20 0 38 7" fill="none" stroke="#222" stroke-width="2" stroke-dasharray="3 3"/><path d="M34 3 L40 8 L33 10" fill="#222"/></svg></a>
</article>

<!-- testimonials -->
<section class="testimonials">
  <div class="map" role="img" aria-label="Faint dotted world map"></div>
  <h2 class="h-display">Testimonials</h2>
  <p class="sub">Lorem ipsum dolor sit amet, consectetur adipiscing elit. Praesent vestibulum sem vel dolor suscipit tempor.</p>
  <div class="avatar" role="img" aria-label="Client portrait photo"></div>
  <svg class="abs" style="left:105px;top:385px" width="40" height="14" viewBox="0 0 40 14"><path d="M38 9 Q20 1 4 8" fill="none" stroke="#333" stroke-width="2" stroke-dasharray="3 3"/><path d="M8 4 L1 9 L8 12" fill="#333"/></svg>
  <svg class="abs" style="left:1055px;top:385px" width="40" height="14" viewBox="0 0 40 14"><path d="M2 9 Q20 1 36 8" fill="none" stroke="#333" stroke-width="2" stroke-dasharray="3 3"/><path d="M32 4 L39 9 L32 12" fill="#333"/></svg>
  <p class="quote">Lorem ipsum dolor sit amet, consectetur adipiscing elit. Praesent vestibulum sem vel dolor suscipit tempor. Quisque ac mauris eget erat fringilla consequat. Quisque maximus ultricies lorem id consequat. Praesent ullamcorper sed nisi eu ultrices. Aliquam a feugiat tellus, eu bibendum est. Curabitur auctor molestie lorem sollicitudin laoreet.</p>
  <div class="stars">
    <svg width="20" height="20" viewBox="0 0 24 24"><path d="M12 2l3 7 7 .6-5.3 4.6 1.7 7.3L12 17.8 5.6 21.5l1.7-7.3L2 9.6 9 9z" fill="var(--gold)"/></svg>
    <svg width="20" height="20" viewBox="0 0 24 24"><path d="M12 2l3 7 7 .6-5.3 4.6 1.7 7.3L12 17.8 5.6 21.5l1.7-7.3L2 9.6 9 9z" fill="var(--gold)"/></svg>
    <svg width="20" height="20" viewBox="0 0 24 24"><path d="M12 2l3 7 7 .6-5.3 4.6 1.7 7.3L12 17.8 5.6 21.5l1.7-7.3L2 9.6 9 9z" fill="var(--gold)"/></svg>
    <svg width="20" height="20" viewBox="0 0 24 24"><path d="M12 2l3 7 7 .6-5.3 4.6 1.7 7.3L12 17.8 5.6 21.5l1.7-7.3L2 9.6 9 9z" fill="var(--gold)"/></svg>
    <svg width="20" height="20" viewBox="0 0 24 24"><path d="M12 2l3 7 7 .6-5.3 4.6 1.7 7.3L12 17.8 5.6 21.5l1.7-7.3L2 9.6 9 9z" fill="var(--gold)"/></svg>
  </div>
  <p class="person">Ravi Castell</p>
  <p class="role">Client</p>
</section>

<!-- footer -->
<footer>
  <h2 class="footer-title">Stay Connected with Ginger Kite Otter</h2>
  <div class="signup">Your Email<svg width="44" height="12" viewBox="0 0 44 12"><path d="M2 8 Q20 0 38 7" fill="none" stroke="#222" stroke-width="2" stroke-dasharray="3 3"/><path d="M34 3 L40 8 L33 10" fill="#222"/></svg></div>
  <nav class="footer-nav"><a>Home</a><a>Services</a><a>Clients</a><a>Testimonials</a><a>About Us</a><a>News</a></nav>
  <p class="footer-call">Call: +44 (0) 7700 900412</p>
  <div class="social" aria-label="Social links"><span></span><span></span><span></span><span></span></div>
  <p class="footer-mail">Email: maren@gingerkiteotter.com</p>
  <p class="copyright">© Copyright 2022.All right reserved &nbsp;&nbsp;&nbsp;|&nbsp;&nbsp;&nbsp; Privacy Policy</p>
  <svg class="abs" style="left:1104px;top:4480px" width="10" height="40" viewBox="0 0 10 40"><path d="M5 38 Q9 20 4 4" fill="none" stroke="#333" stroke-width="2" stroke-dasharray="3 3"/><path d="M1 7 L4 1 L8 6" fill="#333"/></svg>
</footer>

</body>
</html>
```